Label to go onto food packaging.

We need to create a visually interesting and appealing label to stick onto our take away food packaging. The label should contain information of the food products our cafe sells. The label is to go onto biodegradable food bowls and clam shell packaging.
The information is basically the lines we sell - buddha bowls, super smoothies, vegan burgers and curries. And also the slogan 'nourish and refresh'. We have a logo design that we would like to incorporate onto the label (but not essential)
The design will go onto a rectangle strip label.
The colours of our food outlet are splashes of yellow, blue and grey in a white interior.
We also feature a large garden green wall. You may view images from our instagram page bright pebble kitchen

Target Market(s)

Young professional, health conscious, plant based eaters. To be used on takeaway packaging.

Industry/Entity Type

Food Production

Font styles to use
Sans Serif

Colors

Designer to choose colors to be used in the design.

Requirements
Must have
• Bold, appealing, informative.
Nice to have
• Logo incorporated, possibly as a watermark?
Should not have
• No floral shapes. If incorporating the logo, use a circle or nothing around it. No pictures/photos of food

```html
<!DOCTYPE html>
<html lang="en">
<head>
<meta charset="utf-8">
<title>Bright Pebble Kitchen – Takeaway Label</title>
<link href="https://fonts.googleapis.com/css2?family=Great+Vibes&family=Montserrat:wght@300;400;600&display=swap" rel="stylesheet">
<style>
  :root {
    --page: #f2f2f2;
    --label: #ffffff;
    --ink: #6d6d6d;
    --ink-soft: #9a9a9a;
    --gold: #f2c21a;
    --blue: #1f4fb8;
    --lilac: #c9b6f0;
    --sky: #bfe0f7;
    --sun: #f7df6a;
    --cream: #fbf3c4;
    --grey: #d9dbe0;
    --orange: #f39a1e;
    --berry: #b3343a;
  }
  * { margin: 0; padding: 0; box-sizing: border-box; }
  html, body { width: 1200px; height: 1200px; overflow: hidden; background: var(--page); }
  body { font-family: "Montserrat", sans-serif; color: var(--ink); }

  .label {
    position: absolute; left: 442px; top: 10px;
    width: 316px; height: 1180px;
    background: var(--label);
    display: flex; flex-direction: column;
    box-shadow: 0 2px 10px rgba(0,0,0,.08);
  }
  .menu-block { position: relative; text-align: center; padding: 0 10px 8px; }
  .menu-block::before {
    content: ""; position: absolute; left: 0; right: 0; top: 0; height: 38px;
    background: linear-gradient(90deg, var(--lilac), var(--sky) 35%, #fff 60%, var(--sun) 85%, var(--lilac));
    opacity: .75; filter: blur(2px); z-index: 0;
  }
  .menu-block > * { position: relative; z-index: 1; }
  .smoothies { border-top: 1px solid #ddd; }

  .script-title {
    font-family: "Great Vibes", cursive; font-size: 27px; color: var(--gold);
    line-height: 1; padding-top: 7px; height: 38px; font-weight: 400;
  }
  .section-name { font-size: 15px; font-weight: 300; color: #555; letter-spacing: .5px; line-height: 1.1; margin-top: 2px; }
  .item { font-size: 8.6px; line-height: 1.3; font-weight: 300; margin-top: 3px; }
  .diet { display: block; color: var(--ink-soft); }
  .smoothie .item { margin-top: 0; }

  .price-list { width: 190px; margin: 6px auto 0; font-size: 8.4px; font-weight: 300; text-align: left; }
  .price-list .row { display: flex; justify-content: space-between; gap: 8px; line-height: 1.35; }
  .bowls .price-list { width: 225px; margin-top: 10px; }
  .bowls .price-list .row { align-items: flex-end; }
  .bowls .note { border-bottom: 1px solid #bbb; padding-bottom: 3px; }

  .slogan {
    font-family: "Great Vibes", cursive; font-size: 34px; color: var(--blue);
    text-align: center; line-height: 1; padding: 6px 0 4px;
  }

  .burgers {
    text-align: center; padding: 0 12px 10px;
    background:
      radial-gradient(ellipse at 15% 20%, rgba(191,224,247,.9) 0%, transparent 55%),
      radial-gradient(ellipse at 85% 30%, rgba(217,219,224,.9) 0%, transparent 50%),
      linear-gradient(180deg, #fff 0%, var(--sun) 100%);
  }
  .burgers .script-title { padding-top: 6px; }
  .burgers .item { margin-top: 0; }
  .burgers .price-list { margin-top: 6px; }

  .wordmark {
    background: var(--sun);
    font-size: 19px; font-weight: 600; color: #5a5a5a; padding: 2px 8px 4px; line-height: 1.2;
  }
  .diet-keys { display: flex; justify-content: space-around; padding: 6px 8px 4px; background: var(--cream); }
  .key { text-align: center; width: 54px; }
  .key svg { display: block; margin: 0 auto; }
  .key span { display: block; font-size: 5.6px; color: var(--ink-soft); line-height: 1.15; margin-top: 2px; text-transform: uppercase; }

  .footer { flex: 1; background: var(--cream); padding: 4px 8px 4px; }
  .footer-row { display: flex; align-items: center; gap: 10px; }
  .enjoy-by { border: 1.5px solid #222; width: 78px; height: 28px; padding: 1px 4px; color: #222; }
  .enjoy-by small { display: block; font-size: 4.5px; line-height: 1; }
  .enjoy-by strong { display: block; font-size: 11px; text-align: center; line-height: 1; }
  .contact { font-size: 4.8px; line-height: 1.3; color: #444; text-align: center; flex: 1; }
  .net { font-size: 8px; color: #444; margin-top: 4px; }
</style>
</head>
<body>
<main class="label">
  <section class="menu-block bowls">
    <h2 class="script-title">Lunch Buddha Bowls</h2>
    <h3 class="section-name">GOLD</h3>
    <p class="item">Carrot, lentils, avocado, roasted tomato, mushrooms, cabbage, pickled red onion, labne, spiced nuts, rocket<span class="diet">(GF)(VGO)</span></p>
    <p class="item">Freekeh, broccolini, chickpeas, in kale &amp; almond pesto, pickled purple cabbage, beetroot, chia hazel nut dukkah, kefir<span class="diet">(VGO)</span></p>
    <p class="item">Falafel, coconut yoghurt raita, quinoa, pickled cabbage, turmeric roasted cauliflower, rocket, roasted pumpkin<span class="diet">(VG)(GF)</span></p>
    <p class="item">Totopos, avocado salsa, capsicum, corn, black beans, tomato, spicy coconut yoghurt dip<span class="diet">(VG)(GF)</span></p>
    <p class="item">Green tea noodles, edamame, bean shoots, sweet potato, spinach, avocado, kimchi, turtle beans, cucumber<span class="diet">(VG)</span></p>
    <p class="item">Asparagus &amp; cucumber salad, turmeric roasted cauliflower, beetroot noodles, roasted pumpkin, quinoa taboulah, avocado, chickpea and tahini<span class="diet">(V)(GF)(VGO)</span></p>
    <h3 class="section-name">HOT CURRIES</h3>
    <p class="item">pumpkin, coconut, chickpea curry with forbidden black rice, kale, natural yoghurt, nuts and seeds<span class="diet">(GF)(VGO)</span></p>
    <p class="item">Sri lankan cauliflower, sweet potato, zucchini, tomato curry with forbidden black rice, kale, coconut yoghurt<span class="diet">(GF)(VG)</span></p>
    <div class="price-list">
      <div class="row"><span>Add pulled chicken, smoked salmon, tofu</span><span>7</span></div>
      <div class="row"><span>poached egg/goats chevre</span><span>3/4</span></div>
      <div class="row note"><span>Nutrient packed bowls of delicious vibrant vegetables-raw and cooked, legumes, grains, seeds, shoots, with the option of adding a protein</span><span>16.9</span></div>
    </div>
  </section>

  <section class="menu-block smoothies smoothie">
    <h2 class="script-title">Super Smoothies</h2>
    <h3 class="section-name">BUZZ</h3>
    <p class="item">Banana, date, almond milk, raw cacao, bee pollen</p>
    <h3 class="section-name">MATCHA</h3>
    <p class="item">Mango, spinach, avocado, matcha, coconut milk</p>
    <h3 class="section-name">RUN TO PARADISE</h3>
    <p class="item">Berries, acai, coconut water, banana, passion fruit</p>
    <h3 class="section-name">COOL AS A</h3>
    <p class="item">Cucumber, kale, mango, spirulina, ginger, lemon, coconut water</p>
    <h3 class="section-name">MANGO PASH</h3>
    <p class="item">Mango, passion fruit, coconut water, banana, turmeric</p>
    <h3 class="section-name">DREAM</h3>
    <p class="item">Coconut yoghurt, vanilla, cinnamon, chia seeds, banana, coconut water</p>
    <div class="price-list">
      <div class="row"><span>All smoothies</span><span>9.5</span></div>
      <div class="row"><span>Add protein powder</span><span>1.0</span></div>
      <div class="row"><span>Kombucha</span><span>6.9</span></div>
      <div class="row"><span>Sparkling Apple Cider Vinegar</span><span>6.9</span></div>
      <div class="row"><span>Turmeric and Ginger Elixir</span><span>6.9</span></div>
      <div class="row"><span>Mineral Water 250ml/750ml</span><span>3.5/6.5</span></div>
    </div>
  </section>

  <h2 class="slogan">Nourish And Refresh</h2>

  <section class="burgers">
    <h2 class="script-title">Vegan Burgers</h2>
    <h3 class="section-name">GARDEN</h3>
    <p class="item">Beetroot &amp; lentil patty, rocket, pickled onion, cashew aioli</p>
    <h3 class="section-name">SMOKY</h3>
    <p class="item">Black bean patty, avocado, tomato, chipotle coconut yoghurt</p>
    <div class="price-list">
      <div class="row"><span>On toasted vegan bun, with green salad</span><span>15.9</span></div>
      <div class="row"><span>Gluten free bun</span><span>2.0</span></div>
    </div>
  </section>

  <div class="wordmark">bright pebble kitchen</div>

  <div class="diet-keys">
    <div class="key"><svg width="24" height="24" viewBox="0 0 24 24"><circle cx="12" cy="12" r="11" fill="var(--orange)"/><text x="12" y="15" font-size="7" text-anchor="middle" fill="#fff" font-family="Montserrat, sans-serif">VG</text></svg><span>Vegan</span></div>
    <div class="key"><svg width="24" height="24" viewBox="0 0 24 24"><circle cx="12" cy="12" r="11" fill="var(--orange)"/><text x="12" y="15" font-size="7" text-anchor="middle" fill="#fff" font-family="Montserrat, sans-serif">V</text></svg><span>Vegetarian</span></div>
    <div class="key"><svg width="24" height="24" viewBox="0 0 24 24"><circle cx="12" cy="12" r="11" fill="var(--orange)"/><text x="12" y="15" font-size="6.5" text-anchor="middle" fill="#fff" font-family="Montserrat, sans-serif">VGO</text></svg><span>Vegan option<br><b>available</b></span></div>
    <div class="key"><svg width="24" height="24" viewBox="0 0 24 24"><circle cx="12" cy="12" r="11" fill="var(--orange)"/><text x="12" y="15" font-size="7" text-anchor="middle" fill="#fff" font-family="Montserrat, sans-serif">GF</text></svg><span>Gluten<br>free</span></div>
    <div class="key"><svg width="24" height="24" viewBox="0 0 24 24"><circle cx="12" cy="12" r="11" fill="var(--orange)"/><text x="12" y="15" font-size="7" text-anchor="middle" fill="#fff" font-family="Montserrat, sans-serif">DF</text></svg><span>Dairy<br>free</span></div>
  </div>

  <footer class="footer">
    <div class="footer-row">
      <div class="enjoy-by"><small>ENJOY BY</small><strong>3 JAN</strong><small>keep refrigerated</small></div>
      <div class="contact">
        14 Harbour Lane, Seacliff VIC 3190<br>
        03 9000 1234<br>
        hello@brightpebblekitchen.com<br>
        Opening Hours:<br>
        Tuesday to Sunday 8:30am to 4:30pm
      </div>
      <svg width="50" height="22" viewBox="0 0 50 22" aria-hidden="true"><rect x="1" y="2" width="48" height="18" rx="9" fill="#fff" stroke="var(--berry)" stroke-width="1.5"/></svg>
    </div>
    <p class="net">NET WT. 10 OZ (284g)</p>
  </footer>
</main>
</body>
</html>
```